I am looking for help designing my new business cards. I would like rounded edges and a raised logo on the back of the card. I have 2 Logos. One with a boat in it and one without. I'd like the one on the back to be the one that includes the boat and just the name on the front. I have included multiple formats of my logo. Please let me know if you need anymore.

Target Market(s)

Potential buyers and other sales brokers

Industry/Entity Type

Sales - Yacht / Boat Sales

Contact Information for Business Card

Id liike the front to include just the business name portion of the logo along with my name (Corwin Dalby), phone number (555.318.6027), website address (www.dalbymarineco.example) and not my physical address but just "Port Averly, SC". The back should include my full logo that has the boat included. This portion I'd prefer raised amd take up the majority of the space there. Thanks!!

Colors
0054AA
0677BA
7BADD7
CADEEF
E8F1F8
0094D4
00A9DD
6FCCEA
C7EBF8
E9F6FB

Requirements
Must have
• Double sided
Nice to have
• My email address: Corwin@dalbymarineco.example The NMTG logo somewhere small on the front of the card
Should not have
• My full address, prefer only "Port Averly, SC"

```html
<!DOCTYPE html>
<html lang="en">
<head>
<meta charset="utf-8">
<title>Dalby Marine Co — Business Card</title>
<link rel="stylesheet" href="https://fonts.googleapis.com/css2?family=Montserrat:wght@400;500;700;800&display=swap">
<style>
  :root {
    --backdrop: #27335a;
    --card: #f2f5f8;
    --card-edge: #e4eaf0;
    --navy: #1d2d6b;
    --brand-blue: #0054aa;
    --sky: #0094d4;
    --badge: #0677ba;
  }
  * { box-sizing: border-box; margin: 0; padding: 0; }
  html, body {
    width: 1200px; height: 800px; overflow: hidden;
    background: var(--backdrop);
    font-family: "Montserrat", sans-serif;
  }
  .stage {
    position: relative; width: 1200px; height: 800px;
    display: flex; align-items: center; justify-content: center; gap: 44px;
  }
  .card {
    position: relative;
    width: 540px; height: 309px;
    border-radius: 28px;
    background: linear-gradient(135deg, #ffffff 0%, var(--card) 60%, var(--card-edge) 100%);
    overflow: hidden;
  }
  .card-front .wordmark {
    position: absolute; top: 44px; left: 250px;
    display: flex; align-items: center; gap: 8px;
  }
  .wordmark-name {
    font-weight: 800; font-size: 22px; letter-spacing: 1px;
    color: var(--navy); text-transform: uppercase;
    white-space: nowrap;
  }
  .wordmark-dot {
    width: 10px; height: 10px; border-radius: 50%; background: var(--sky);
  }
  .partner-badge {
    position: absolute; top: 140px; left: 38px;
    width: 58px; height: 34px; border-radius: 4px;
    background: var(--badge);
  }
  .contact-list {
    position: absolute; top: 108px; left: 290px;
    list-style: none;
    font-size: 12.5px; font-weight: 400; color: var(--navy);
    line-height: 22px;
    white-space: nowrap;
  }
  .contact-list li { display: flex; align-items: center; gap: 12px; }
  .contact-list li::before {
    content: ""; width: 5px; height: 5px; background: var(--sky); flex: none;
  }
  .holder {
    position: absolute; left: 112px; bottom: 40px;
  }
  .holder-name {
    font-weight: 700; font-size: 19px; letter-spacing: 0.8px;
    color: var(--navy); text-transform: uppercase;
    white-space: nowrap;
  }
  .holder-title {
    margin-top: 4px; font-size: 13px; font-weight: 400; color: var(--brand-blue);
  }
  .card-back {
    display: flex; align-items: center; justify-content: center;
  }
  .back-mark {
    display: flex; flex-direction: column; align-items: center; gap: 12px;
  }
  .back-mark .mark-art {
    width: 230px; height: 96px; border-radius: 10px;
    background: linear-gradient(160deg, #e9f6fb 0%, #7badd7 55%, #0094d4 100%);
  }
  .back-mark .wordmark-name { font-size: 34px; letter-spacing: 1.5px; }
</style>
</head>
<body>
<main class="stage">
  <section class="card card-front" aria-label="Business card front">
    <div class="wordmark">
      <span class="wordmark-name">Dalby Marine Co</span>
      <span class="wordmark-dot"></span>
    </div>
    <div class="partner-badge" role="img" aria-label="Membership badge of NMTG"></div>
    <ul class="contact-list">
      <li>(555) 318-6027</li>
      <li>corwin@dalbymarineco.example</li>
      <li>www.dalbymarineco.example</li>
      <li>Port Averly, SC</li>
    </ul>
    <div class="holder">
      <p class="holder-name">Corwin Dalby</p>
      <p class="holder-title">Founder &amp; CEO</p>
    </div>
  </section>

  <section class="card card-back" aria-label="Business card back">
    <div class="back-mark">
      <div class="mark-art" role="img" aria-label="Raised logo illustration of a center-console boat riding a wave"></div>
      <span class="wordmark-name">Dalby Marine Co</span>
    </div>
  </section>
</main>
</body>
</html>
```